Personal Biography Website for a Professional Game Developer

I'm looking for someone to design a personal biography website for a professional game developer. Look at the attached logos, headshots, and art as examples of the type of style that I'm looking for. This should be an edgy, progressive-style website -- like one you'd expect from a video game website.
I'm also a huge fan of the brelt website... large images for each section with little text.
I've attached the bio text as well (the underlines are just place holders)
Target Market(s)
Venture Capital, Video Game Developers
Number of Pages Required
1 page
Look and feel
Each slider illustrates characteristics of the customer's brand and the style your logo design should communicate.

```html
<!DOCTYPE html>
<html lang="en">
<head>
<meta charset="utf-8">
<title>Marco Delvani — Game Developer</title>
<link href="https://fonts.googleapis.com/css2?family=Montserrat:wght@400;500;600;700;800;900&display=swap" rel="stylesheet">
<style>
:root{
  --bg:#000;
  --ink:#fff;
  --cyan:#1cc4f2;
  --blue:#1597d6;
  --navy:#2b2f6b;
  --red:#e8212e;
  --muted:#d8d8e0;
  --grad:linear-gradient(90deg,var(--cyan) 0%,var(--cyan) 35%,var(--navy) 50%,var(--red) 78%);
}
*{margin:0;padding:0;box-sizing:border-box}
html,body{width:1200px;height:2649px;overflow:hidden;background:var(--bg)}
body{position:relative;font-family:'Montserrat',sans-serif;color:var(--ink)}
.abs{position:absolute}
.grad-text{background:var(--grad);-webkit-background-clip:text;background-clip:text;color:transparent}
.btn{position:absolute;height:42px;border:1.5px solid #fff;border-radius:22px;display:flex;align-items:center;justify-content:center;font-size:13px;font-weight:500;letter-spacing:.3px;color:#fff;text-decoration:none}
.dash{position:absolute;height:3px}
.dash.c{background:var(--blue)}
.dash.r{background:var(--red)}
.dash.w{background:#fff}
.social{display:flex;gap:7px}
.social span{width:35px;height:35px;border:1.5px solid #cfd3dc;border-radius:50%;display:block}

/* header */
.brand{left:141px;top:22px;font-size:34px;font-weight:800;color:var(--cyan);letter-spacing:1px}
.nav{left:607px;top:33px;display:flex;gap:0;font-size:13px;font-weight:500}
.nav a{color:#fff;text-decoration:none;position:absolute;white-space:nowrap}
.nav .active::after{content:"";position:absolute;left:0;right:0;bottom:-9px;height:2px;background:linear-gradient(90deg,var(--cyan),var(--red))}
.hero-photo{left:560px;top:0;width:640px;height:710px;background:radial-gradient(ellipse at 55% 35%,#1d5f8c 0%,#143a6a 28%,#2a0f2a 52%,#000 75%)}
.hero-title{left:139px;top:222px;font-size:76px;font-weight:800;line-height:1}
.hero-sub{left:140px;top:391px;font-size:19px;font-weight:400}

/* gaming */
.rocks{left:0;top:850px;width:1200px;height:260px;background:linear-gradient(180deg,#000 0%,#2a2e38 35%,#1b1e26 65%,#000 100%)}
.section-title{font-size:42px;font-weight:800;letter-spacing:.5px;white-space:nowrap}
.gaming-title{left:0;width:1200px;top:790px;text-align:center}
.gaming-text{left:0;width:1200px;top:846px;text-align:center;font-size:14.5px;line-height:24px;color:var(--muted)}

/* work */
.emblem{left:141px;top:1190px;width:360px;height:515px;background:linear-gradient(160deg,#9c1b22 0%,#176a9e 45%,#9c1b22 75%,#0f4f78 100%);border-radius:46% 46% 30% 30%;opacity:.85}
.work-title{left:566px;top:1290px}
.work-text{left:566px;top:1353px;width:500px;font-size:14.5px;line-height:24px;color:var(--muted)}
.work-list{left:566px;top:1412px;list-style:none;font-size:14.5px;color:var(--muted)}
.work-list li{height:31.7px;display:flex;align-items:center;gap:7px}
.tick{width:16px;height:16px;flex:none}

/* passion */
.portrait{left:680px;top:1790px;width:520px;height:672px;background:radial-gradient(ellipse at 40% 40%,#3a2a7a 0%,#25378a 40%,#1c6aa8 70%,#0c0c2a 100%)}
.grid-glow{left:0;top:1760px;width:1200px;height:702px;background:linear-gradient(180deg,#000 0%,#1b0610 40%,#000 100%);opacity:.6}
.passion{left:145px;top:1985px;font-size:36px;font-weight:700;line-height:53px;letter-spacing:.4px}
.passion-accent{left:143px;top:2150px;font-size:42px;font-weight:800;letter-spacing:.4px}

/* contact band */
.band{left:0;top:2462px;width:1200px;height:124px;background:linear-gradient(90deg,#22cdf6 0%,#2f6aa8 22%,#2d2b64 45%,#6b1c45 68%,#d21e30 88%,#ee2530 100%)}
.info{position:absolute;top:0;height:124px;display:flex;align-items:center;gap:16px;font-size:13px;font-weight:600;line-height:23px}
.info .big{font-size:15px;font-weight:600}
.icon{width:50px;height:50px;border:1.5px solid #fff;border-radius:50%;display:flex;align-items:center;justify-content:center;flex:none}
.divider{position:absolute;top:0;width:1px;height:124px;background:rgba(255,255,255,.18)}
.footer-copy{left:141px;top:2610px;font-size:13px;color:#ddd}
</style>
</head>
<body>

<!-- header -->
<div class="abs hero-photo" role="img" aria-label="Portrait photo of the developer lit in blue and red"></div>
<div class="abs brand">DELVANI</div>
<nav class="abs nav">
  <a class="active" style="left:0">HOME</a>
  <a style="left:103px">BIO</a>
  <a style="left:180px">CONTACT</a>
</nav>
<div class="abs social" style="left:897px;top:25px"><span></span><span></span><span></span><span></span></div>

<div class="dash c" style="left:285px;top:113px;width:19px"></div>
<div class="dash w" style="left:82px;top:159px;width:15px"></div>
<div class="dash c" style="left:173px;top:175px;width:19px"></div>
<div class="dash r" style="left:51px;top:200px;width:46px"></div>

<h1 class="abs hero-title"><span class="grad-text" style="display:block">MARCO</span></h1>
<svg class="abs" style="left:139px;top:305px" width="560" height="80" viewBox="0 0 560 80" aria-label="DELVANI">
  <defs><linearGradient id="outline" x1="0" x2="1"><stop offset="0" stop-color="#1cc4f2"/><stop offset=".45" stop-color="#2b2f6b"/><stop offset="1" stop-color="#e8212e"/></linearGradient></defs>
  <text x="0" y="68" font-family="Montserrat,sans-serif" font-weight="500" font-size="76" fill="none" stroke="url(#outline)" stroke-width="2.5">DELVANI</text>
</svg>
<p class="abs hero-sub">I Am Professional Game Developer</p>
<a class="btn" style="left:141px;top:445px;width:151px">CONTACT ME</a>
<a class="btn" style="left:307px;top:445px;width:115px">READ BIO</a>
<div class="dash c" style="left:539px;top:481px;width:19px"></div>
<div class="dash r" style="left:480px;top:509px;width:44px"></div>
<div class="dash c" style="left:386px;top:529px;width:15px"></div>

<!-- gaming technology -->
<div class="abs rocks" role="img" aria-label="Dark rocky landscape artwork"></div>
<h2 class="abs section-title gaming-title"><span class="grad-text">GAMING TECHNOLOGY</span></h2>
<p class="abs gaming-text">Having a genuine passion for translating cinematic blueprints into tangible realities and doing so all while<br>ensuring everyone involved has positive constructive experiences along the way.</p>

<!-- work experience -->
<div class="dash c" style="left:552px;top:1143px;width:19px"></div>
<div class="dash w" style="left:760px;top:1189px;width:14px"></div>
<div class="dash c" style="left:665px;top:1205px;width:19px"></div>
<div class="dash r" style="left:760px;top:1230px;width:45px"></div>

<div class="abs emblem" role="img" aria-label="Illustrated emblem of the developer in red and blue"></div>
<h2 class="abs section-title work-title"><span class="grad-text">WORK EXPERIENCE</span></h2>
<p class="abs work-text">Lorem ipsum dolor sit amet, consectetuer adipiscing elit sed nonumy nibh euismod tincidunt ut laoreet dolore magna aliquam.</p>
<ul class="abs work-list">
  <li><svg class="tick" viewBox="0 0 16 16"><circle cx="8" cy="8" r="8" fill="#2a5aa8"/><path d="M4.5 8.2l2.3 2.3 4.7-5" stroke="#fff" stroke-width="1.8" fill="none"/></svg>Ut wisi enim ad minim veniam quis nostrud exerci.</li>
  <li><svg class="tick" viewBox="0 0 16 16"><circle cx="8" cy="8" r="8" fill="#2a5aa8"/><path d="M4.5 8.2l2.3 2.3 4.7-5" stroke="#fff" stroke-width="1.8" fill="none"/></svg>Consectetuer adipiscing elit diam nonummy.</li>
  <li><svg class="tick" viewBox="0 0 16 16"><circle cx="8" cy="8" r="8" fill="#2a5aa8"/><path d="M4.5 8.2l2.3 2.3 4.7-5" stroke="#fff" stroke-width="1.8" fill="none"/></svg>Duis autem vel eum iriure dolor in hendrerit in molestie.</li>
  <li><svg class="tick" viewBox="0 0 16 16"><circle cx="8" cy="8" r="8" fill="#2a5aa8"/><path d="M4.5 8.2l2.3 2.3 4.7-5" stroke="#fff" stroke-width="1.8" fill="none"/></svg>Eum iriure dolor in hendrerit in vulputate velit esse molestie.</li>
</ul>
<a class="btn" style="left:566px;top:1557px;width:151px">CONTACT ME</a>
<div class="dash c" style="left:844px;top:1569px;width:19px"></div>
<div class="dash r" style="left:878px;top:1598px;width:46px"></div>
<div class="dash c" style="left:1001px;top:1617px;width:15px"></div>

<!-- passion -->
<div class="abs grid-glow"></div>
<div class="abs portrait" role="img" aria-label="Close-up portrait photo of the developer in purple and blue tones"></div>
<div class="dash c" style="left:455px;top:1820px;width:19px"></div>
<div class="dash w" style="left:662px;top:1866px;width:15px"></div>
<div class="dash c" style="left:567px;top:1883px;width:19px"></div>
<div class="dash r" style="left:662px;top:1907px;width:46px"></div>

<p class="abs passion">Passionately Accentuating<br>The Gaming/Entertainment<br>Experience For The</p>
<p class="abs passion-accent"><span class="grad-text">Last 10+ Years.</span></p>
<a class="btn" style="left:142px;top:2237px;width:151px">CONTACT ME</a>
<a class="btn" style="left:309px;top:2237px;width:115px">READ BIO</a>
<div class="dash c" style="left:103px;top:2291px;width:19px"></div>
<div class="dash r" style="left:137px;top:2319px;width:45px"></div>
<div class="dash c" style="left:260px;top:2338px;width:15px"></div>

<!-- contact band -->
<section class="abs band">
  <div class="info" style="left:141px">
    <div class="icon"><svg width="26" height="26" viewBox="0 0 26 26" fill="none" stroke="#fff" stroke-width="1.5"><circle cx="13" cy="13" r="10"/><path d="M3 13h20M13 3c4 4 4 16 0 20M13 3c-4 4-4 16 0 20"/></svg></div>
    <div>123, Building Name, Street<br>City, State XY 123456</div>
  </div>
  <div class="divider" style="left:445px"></div>
  <div class="info" style="left:516px">
    <div class="icon"><svg width="24" height="24" viewBox="0 0 24 24" fill="none" stroke="#fff" stroke-width="1.5"><path d="M5 3l4 1 1 4-2 2c1 3 3 5 6 6l2-2 4 1 1 4-2 2C10 21 3 14 3 5z"/></svg></div>
    <div>PHONE<br><span class="big">(123) 456 7890</span></div>
  </div>
  <div class="divider" style="left:767px"></div>
  <div class="info" style="left:838px">
    <div class="icon"><svg width="24" height="24" viewBox="0 0 24 24" fill="none" stroke="#fff" stroke-width="1.5"><rect x="3" y="9" width="18" height="12"/><path d="M3 9l9 7 9-7M6 11V3h12v8"/></svg></div>
    <div>EMAIL<br>info@marcodelvani.com</div>
  </div>
</section>

<!-- footer -->
<p class="abs footer-copy">Copyright 2022. MarcoDelvani. All Rights Reserved</p>
<div class="abs social" style="left:894px;top:2600px"><span></span><span></span><span></span><span></span></div>

</body>
</html>
```